Communication Skill: GLOW Bridge

I need a Design for a skill I teach to youth. That's why the title GLOW Bridge. GLOW stands for Thoughts, Emotions, Concerns, Hopes & Desires. Under each word are some examples that are meant to help people discuss certain things. I tried to create something myself but want something much more creative and dynamic. I have attached what I designed because it has the information I need in the design. Want it to have a techie look to it.

```html
<!DOCTYPE html>
<html lang="en">
<head>
<meta charset="utf-8">
<title>GLOW Bridge</title>
<link rel="stylesheet" href="https://fonts.googleapis.com/css2?family=Oxanium:wght@400;700&family=Arimo:wght@400&display=swap">
<style>
  :root {
    --bg: #e1e8e7;
    --accent: #4cf5c2;
    --ink: #8f8f8f;
    --line: #8c8c8c;
    --white: #ffffff;
  }
  * { margin: 0; padding: 0; box-sizing: border-box; }
  html, body { width: 1200px; height: 849px; overflow: hidden; background: var(--bg); }
  .poster { position: relative; width: 1200px; height: 849px; background: var(--bg); }
  .connectors { position: absolute; left: 0; top: 0; }
  .title {
    position: absolute; left: 595px; top: 103px; transform: translate(-50%, -50%);
    font-family: "Oxanium", sans-serif; font-weight: 700; font-size: 94px;
    letter-spacing: 3px; color: var(--accent); white-space: nowrap; line-height: 1;
  }
  .pillar-heading {
    position: absolute; transform: translate(-50%, -50%);
    font-family: "Oxanium", sans-serif; font-weight: 400; font-size: 38px;
    letter-spacing: 1px; color: var(--white); white-space: nowrap; line-height: 1;
  }
  .pillar-heading .initial { color: var(--accent); font-weight: 700; }
  .prompt {
    position: absolute; transform: translate(-50%, -50%);
    font-family: "Arimo", sans-serif; font-size: 17px; color: var(--ink);
    white-space: nowrap; line-height: 1; letter-spacing: 0.2px;
  }
</style>
</head>
<body>
<main class="poster">
  <svg class="connectors" width="1200" height="849" viewBox="0 0 1200 849" aria-hidden="true">
    <g fill="none" stroke="var(--line)" stroke-width="1.5">
      <polyline points="216,102 143,102 143,278"/>
      <line x1="443" y1="181" x2="443" y2="280"/>
      <line x1="751" y1="181" x2="751" y2="279"/>
      <polyline points="977,102 1051,102 1051,279"/>
    </g>
    <g fill="var(--white)" stroke="var(--line)" stroke-width="1.5">
      <circle cx="143" cy="287" r="9"/>
      <circle cx="443" cy="289" r="9"/>
      <circle cx="751" cy="288" r="9"/>
      <circle cx="1051" cy="288" r="9"/>
    </g>
  </svg>

  <h1 class="title">GLOW BRIDGE</h1>

  <h2 class="pillar-heading" style="left:144px; top:335px;"><span class="initial">T</span>HOUGHTS</h2>
  <h2 class="pillar-heading" style="left:436px; top:335px;"><span class="initial">E</span>MOTIONS</h2>
  <h2 class="pillar-heading" style="left:749px; top:335px;"><span class="initial">C</span>ONCERNS</h2>
  <h2 class="pillar-heading" style="left:1050px; top:330px;"><span class="initial">H</span>OPES</h2>

  <section class="pillar thoughts">
    <p class="prompt" style="left:151px; top:400px;">IT SEEMS…</p>
    <p class="prompt" style="left:151px; top:442px;">I WONDER…</p>
    <p class="prompt" style="left:151px; top:484px;">IT’S MY OPINION…</p>
    <p class="prompt" style="left:151px; top:526px;">I BELIEVE…</p>
    <p class="prompt" style="left:151px; top:568px;">I ASSUME…</p>
    <p class="prompt" style="left:151px; top:611px;">I THINK…</p>
  </section>

  <section class="pillar emotions">
    <p class="prompt" style="left:443px; top:399px;">I’M…</p>
    <p class="prompt" style="left:443px; top:450px;">HOPEFUL</p>
    <p class="prompt" style="left:443px; top:481px;">WORRIED</p>
    <p class="prompt" style="left:443px; top:512px;">SAD</p>
    <p class="prompt" style="left:443px; top:542px;">AFRAID</p>
    <p class="prompt" style="left:443px; top:573px;">MAD</p>
    <p class="prompt" style="left:443px; top:604px;">GLAD</p>
    <p class="prompt" style="left:443px; top:635px;">HAPPY</p>
    <p class="prompt" style="left:443px; top:665px;">CONFIDENT</p>
    <p class="prompt" style="left:443px; top:696px;">INSECURE</p>
    <p class="prompt" style="left:443px; top:727px;">LONELY</p>
    <p class="prompt" style="left:443px; top:757px;">BOTHERED</p>
    <p class="prompt" style="left:443px; top:788px;">UNCERTAIN</p>
  </section>

  <section class="pillar concerns">
    <p class="prompt" style="left:756px; top:401px;">I WORRY ABOUT…</p>
    <p class="prompt" style="left:756px; top:442px;">I’M AFRAID THAT…</p>
    <p class="prompt" style="left:756px; top:483px;">I’M NERVOUS BECAUSE…</p>
    <p class="prompt" style="left:756px; top:524px;">IT BOTHERS ME THAT…</p>
  </section>

  <section class="pillar hopes">
    <p class="prompt" style="left:1051px; top:399px;">I HOPE…</p>
    <p class="prompt" style="left:1051px; top:441px;">I WISH…</p>
    <p class="prompt" style="left:1051px; top:482px;">IT’S MY DESIRE…</p>
    <p class="prompt" style="left:1051px; top:523px;">I’D LIKE TO SEE…</p>
    <p class="prompt" style="left:1051px; top:565px;">I WANT…</p>
    <p class="prompt" style="left:1051px; top:606px;">I NEED…</p>
  </section>
</main>
</body>
</html>
```